Kestin Power Battery advertisment for Facebook ads

Objective:
Design a compelling Facebook advertisement to promote the new Federal Government Home Battery Subsidy, encouraging existing solar customers to act now and install a battery system under the new subsidy program.

Key Message:

25kWh Battery System Installed from $9,800
Act now and secure your affordable energy future today!
Design Requirements:

Bold headline showcasing the 25kWh for $9,800 offer.
Clear reference to the Federal Government Battery Subsidy as the reason for the low pricing.
Include messaging around:
Claim your subsidy before it winds down—like the solar rebate, it reduces each year
The subsidy can only be claimed once per household—go large now to future-proof your energy needs
Add a strong Call to Action like: “Beat the Rush—Secure Your Battery Today!”

Target Market(s)

Home owners who want to add batteries to existing solar systems

Industry/Entity Type

Renewable energy

Colors
0054AA
0677BA
7BADD7
CADEEF
E8F1F8
EB3D1F
EC4F4E
F09395
F8D3D4
FCEDEE

Requirements
Must have
• Visual Style: Modern, clean, and high-trust Use imagery of solar homes, battery units, or families enjoying power security at night Include visual cues of savings, energy independence, or clean energy Mobile-optimized, designed for Facebook feed
Nice to have
• Tone: Confident, future-focused, and urgent—while remaining trustworthy and informative. I would like a picture of battery ideally VOM battery on a home or such
Should not have
• must be professional and be a call to action

```html
<!DOCTYPE html>
<html lang="en">
<head>
<meta charset="utf-8">
<title>Kestin Power – 25kWh Battery System Ad</title>
<link href="https://fonts.googleapis.com/css2?family=Montserrat:wght@300;400;500;700;800;900&display=swap" rel="stylesheet">
<style>
  :root {
    --stage: #bfbfc0;
    --sky-top: #00aeef;
    --sky-mid: #3fbfd8;
    --aqua: #8dd6cc;
    --white: #ffffff;
    --ink: #111111;
    --band: #000000;
    --sun-yellow: #f5d41c;
    --sun-orange: #ee4f2a;
    --leaf: #6cc04a;
    --blue-line: #1c9ad6;
    --amber: #e8a12a;
    --amber-deep: #c66a1a;
    --home-panel: #5d7396;
    --home-wall: #e4ddd0;
    --home-green: #7fae55;
  }
  * { margin: 0; padding: 0; box-sizing: border-box; }
  html, body {
    width: 1200px; height: 849px; overflow: hidden;
    background: var(--stage);
  }
  .ad {
    position: absolute; left: 200px; top: 24px;
    width: 800px; height: 800px; overflow: hidden;
    font-family: "Montserrat", sans-serif;
    background: linear-gradient(180deg, var(--sky-top) 0%, var(--sky-top) 14%, var(--sky-mid) 34%, var(--aqua) 50%, #d4efec 60%, var(--white) 64%);
  }
  .ad__art { position: absolute; inset: 0; width: 800px; height: 800px; }
  .headline {
    position: absolute; left: 49px; top: 72px;
    color: var(--white); font-weight: 800; font-size: 56px; line-height: 64px;
    letter-spacing: 0.5px;
  }
  .price {
    position: absolute; left: 46px; top: 196px;
    color: var(--white); font-weight: 300; font-size: 44px; letter-spacing: 0.5px;
    white-space: nowrap;
  }
  .price__amount { font-weight: 800; position: relative; }
  .price__amount::after {
    content: ""; position: absolute; left: 2px; right: 2px; bottom: -6px; height: 3px;
    background: linear-gradient(90deg, var(--sun-yellow), var(--sun-orange));
  }
  .subsidy {
    position: absolute; left: 58px; top: 274px; width: 335px;
    color: var(--ink); font-weight: 500; font-size: 22.5px; line-height: 26px;
    padding-bottom: 6px;
  }
  .subsidy::after {
    content: ""; position: absolute; left: 0; right: 0; bottom: -4px; height: 2.5px;
    background: linear-gradient(90deg, var(--leaf), var(--blue-line));
  }
  .notice {
    position: absolute; left: 145px; top: 376px; width: 262px;
    color: var(--ink); font-size: 17px; line-height: 21.5px; font-weight: 300;
  }
  .notice strong { font-weight: 700; }
  .once {
    position: absolute; left: 64px; top: 488px; width: 320px;
    color: var(--ink); font-size: 19px; line-height: 27.5px; font-weight: 300;
  }
  .once strong { font-weight: 900; display: block; }
  .cta {
    position: absolute; left: 0; width: 800px; top: 688px; padding-left: 30px;
    text-align: center; color: var(--white);
    font-weight: 900; font-size: 30.5px; line-height: 37px;
  }
</style>
</head>
<body>
  <main class="ad">
    <svg class="ad__art" viewBox="0 0 1248 1248">
      <defs>
        <linearGradient id="amberPhoto" x1="0" y1="1" x2="1" y2="0">
          <stop offset="0" stop-color="#f3d22a"/>
          <stop offset="0.45" stop-color="var(--amber)"/>
          <stop offset="1" stop-color="var(--amber-deep)"/>
        </linearGradient>
        <linearGradient id="homePhoto" x1="0" y1="0" x2="0.6" y2="1">
          <stop offset="0" stop-color="var(--home-panel)"/>
          <stop offset="0.5" stop-color="var(--home-wall)"/>
          <stop offset="1" stop-color="var(--home-green)"/>
        </linearGradient>
        <linearGradient id="unitPhoto" x1="0" y1="0" x2="1" y2="0">
          <stop offset="0" stop-color="#e6e8ea"/>
          <stop offset="0.5" stop-color="#ffffff"/>
          <stop offset="1" stop-color="#d2d5d8"/>
        </linearGradient>
        <linearGradient id="ringGrad" x1="0" y1="0" x2="1" y2="0">
          <stop offset="0" stop-color="var(--leaf)"/>
          <stop offset="1" stop-color="var(--blue-line)"/>
        </linearGradient>
      </defs>

      <polygon class="photo-wall-batteries" role="img" aria-label="Photo of wall-mounted home battery units in warm light"
        fill="url(#amberPhoto)"
        points="1001,0 1248,0 1248,77 1148,202 1248,227 1248,422 1100,560 990,560 1031,455 781,390"/>

      <rect class="photo-solar-home" role="img" aria-label="Photo of a modern home with rooftop solar panels and trees"
        x="690" y="560" width="558" height="420" rx="18" fill="url(#homePhoto)"/>

      <rect class="cta-band" x="0" y="1022" width="1248" height="226" fill="var(--band)"/>

      <g class="photo-battery-units" role="img" aria-label="Photos of white stackable home battery units">
        <rect x="41" y="987" width="102" height="190" rx="4" fill="url(#unitPhoto)"/>
        <rect x="157" y="1048" width="98" height="138" rx="4" fill="url(#unitPhoto)"/>
      </g>
      <g class="photo-battery-units" role="img" aria-label="Photos of white stackable home battery units">
        <rect x="1050" y="992" width="92" height="196" rx="4" fill="url(#unitPhoto)"/>
        <rect x="1160" y="1072" width="64" height="116" rx="4" fill="url(#unitPhoto)"/>
      </g>

      <g class="callout-frame">
        <path d="M136,573 H609 a66,66 0 0 1 0,132 H136" fill="var(--white)" stroke="url(#ringGrad)" stroke-width="3"/>
        <circle cx="136" cy="639" r="66" fill="var(--white)" stroke="url(#ringGrad)" stroke-width="3"/>
        <path d="M124,600 H146 L140,652 H130 Z" fill="url(#ringGrad)"/>
        <circle cx="135" cy="669" r="11" fill="url(#ringGrad)"/>
      </g>
    </svg>

    <h1 class="headline">25kWh<br>Battery System</h1>
    <p class="price">Installed from <span class="price__amount">$9,800</span></p>
    <p class="subsidy">Through The Federal Government Battery Subsidy</p>
    <p class="notice">Claim your subsidy before it winds down—<strong>like the solar rebate, it reduces each year</strong></p>
    <p class="once">The subsidy can only be claimed once per household—<strong>go large now to future-proof your energy needs.</strong></p>
    <p class="cta">Beat the Rush —<br>Secure Your Battery Today!</p>
  </main>
</body>
</html>
```